Company portfolio catalog

Our company - "The Velvet Nook" specializes in soft furnishings such as:
- curtains
- blinds
- wallpaper
- solar films
- re-upholstery

We also carry prestigious brands such as Marlow Pennick, Vextra motors and Orlena fabrics.

See our website - www.thevelvetnook-example.com.sg
our logo, showroom pic as attached

We want the feel to be a little fun and sleek as we're dealing with interior, but yet look expensive and classy....

Industry/Entity Type

Boutique

```html
<!DOCTYPE html>
<html lang="en">
<head>
<meta charset="utf-8">
<title>The Velvet Nook – Company Portfolio Catalog</title>
<link rel="stylesheet" href="https://fonts.googleapis.com/css2?family=Arvo:wght@400;700&family=Dancing+Script:wght@700&family=Open+Sans:wght@400&family=Quicksand:wght@400&display=swap">
<style>
  :root {
    --backdrop: #e9e7e3;
    --ink-black: #0d0d0e;
    --page-dark: #2a2c2f;
    --page-mid: #4b4e52;
    --band-grey: #c9c9c9;
    --text-light: #e6e6e6;
    --text-soft: #c3c5c8;
    --circle-fill: #ffffff;
    --circle-ring: #8a8d91;
    --circle-text: #1c1c1e;
    --showroom-a: #d9d6d1;
    --showroom-b: #5a5b5e;
    --bedroom-a: #b9b7b3;
    --bedroom-b: #3a3632;
  }
  * { box-sizing: border-box; margin: 0; padding: 0; }
  html, body { width: 1200px; height: 900px; overflow: hidden; }
  body { background: var(--backdrop); position: relative; font-family: "Open Sans", sans-serif; }

  .cover, .spread { position: absolute; top: 210px; height: 480px; box-shadow: 0 10px 30px rgba(0,0,0,.18); }

  /* Cover */
  .cover { left: 40px; width: 340px; background: var(--ink-black); overflow: hidden; }
  .cover__masthead { position: absolute; top: 0; left: 0; width: 100%; height: 200px; text-align: center; }
  .cover__name { position: absolute; top: 108px; width: 100%; font-family: "Quicksand", sans-serif; font-weight: 400; font-size: 31px; color: var(--text-soft); letter-spacing: .2px; }
  .cover__tagline { position: absolute; top: 156px; width: 100%; font-family: "Dancing Script", cursive; font-weight: 700; font-size: 17px; color: #ffffff; letter-spacing: .6px; }
  .cover__band { position: absolute; top: 200px; left: 0; width: 100%; height: 9px; background: var(--band-grey); }
  .cover__photo { position: absolute; top: 209px; left: 0; width: 100%; height: 271px; background: linear-gradient(100deg, var(--showroom-b) 0%, #8f8f92 35%, var(--showroom-a) 65%, #f1efec 80%, #7a7b7e 100%); }

  /* Spread */
  .spread { left: 440px; width: 720px; display: flex; }
  .page { width: 360px; height: 100%; position: relative; overflow: hidden; }
  .page--info { background: linear-gradient(160deg, var(--page-dark) 0%, #35383b 55%, var(--page-mid) 100%); color: var(--text-soft); }
  .page--photo { background: linear-gradient(115deg, #6d6b68 0%, var(--bedroom-a) 35%, #e2e0dc 50%, #8a8681 70%, var(--bedroom-b) 100%); }

  .section-title { position: absolute; left: 24px; font-family: "Arvo", serif; font-weight: 400; font-size: 23px; line-height: 1.2; color: var(--text-light); letter-spacing: .5px; }
  .copy { position: absolute; font-size: 6.6px; line-height: 1.55; color: var(--text-soft); }
  .copy--left { left: 24px; width: 150px; }
  .copy--right { left: 190px; width: 150px; }
  .bullets { list-style: none; }
  .bullets li { margin-bottom: 2px; }

  .about-title { top: 22px; }
  .about-copy { top: 56px; }
  .services-title { top: 146px; }
  .services-copy { top: 180px; }
  .products-title { top: 258px; }

  .product { position: absolute; width: 78px; height: 78px; border-radius: 50%; background: radial-gradient(circle at 40% 35%, var(--circle-fill) 0%, #ececec 70%, #d8d8d8 100%); border: 4px solid var(--circle-ring); display: flex; align-items: center; justify-content: center; text-align: center; font-family: "Arvo", serif; font-weight: 700; font-size: 11px; line-height: 1.1; color: var(--circle-text); }
  .product--blinds   { left: 28px;  top: 304px; }
  .product--curtains { left: 126px; top: 300px; }
  .product--brand    { left: 224px; top: 294px; font-size: 10px; }
  .product--blank-a  { left: 44px;  top: 388px; }
  .product--films    { left: 142px; top: 384px; }
  .product--blank-b  { left: 240px; top: 378px; }
</style>
</head>
<body>
  <section class="cover">
    <header class="cover__masthead">
      <h1 class="cover__name">The Velvet Nook</h1>
      <p class="cover__tagline">Premium Soft Furnishings</p>
    </header>
    <div class="cover__band"></div>
    <div class="cover__photo" role="img" aria-label="Showroom interior with curtains, roller blinds and a bright window"></div>
  </section>

  <section class="spread">
    <article class="page page--info">
      <h2 class="section-title about-title">ABOUT US</h2>
      <p class="copy copy--left about-copy">The Velvet Nook specialises in quality soft furnishings such as curtains, blinds, wallpaper and window films. We offer a wide range of fabrics and styles, from timeless classics to modern looks, all tailored to your home or office space.</p>
      <p class="copy copy--right about-copy">We believe in creating the right ambience for the spaces you live, work or relax in. The Velvet Nook is based in Singapore and has a portfolio of residential and commercial projects. Contact us today.</p>

      <h2 class="section-title services-title">SERVICES</h2>
      <p class="copy copy--left services-copy">The Velvet Nook prides itself in delivering quality designer curtains, blinds, roller screens, wallpaper and window films. In addition, we provide hassle-free installation services including:</p>
      <ul class="copy copy--right services-copy bullets">
        <li>Professional and friendly consultation</li>
        <li>Free onsite measurement</li>
        <li>Non-obligatory quotation via phone or email</li>
        <li>Fuss-free installation with excellent workmanship</li>
      </ul>

      <h2 class="section-title products-title">PRODUCTS</h2>
      <div class="product product--blinds">BLINDS</div>
      <div class="product product--curtains">CURTAINS</div>
      <div class="product product--brand">MARLOW<br>PENNICK<br>WINDOW<br>FASHIONS</div>
      <div class="product product--blank-a"></div>
      <div class="product product--films">WINDOW<br>FILMS</div>
      <div class="product product--blank-b"></div>
    </article>
    <article class="page page--photo" role="img" aria-label="Bedroom with upholstered bed, grey throw, slatted wall panels and a bedside lamp"></article>
  </section>
</body>
</html>
```